Website for Excavator and Earthworks Company

We require a modern, sleek and practical website for our newly created earthworks/excavator business in Perth, Western Australia called Gullwind Stonecut Earthworks.

The website should have a modern, cutting edge feel but only needs to be relatively simplistic in it's layout and eventual functionality.

Some pages it should have would be Home, About, Projects and Contact Us.

Number of Pages Required

1 page

```html
<!DOCTYPE html>
<html lang="en">
<head>
<meta charset="utf-8">
<title>Gullwind Stonecut Earthworks</title>
<link rel="stylesheet" href="https://fonts.googleapis.com/css2?family=Orbitron:wght@500;600&family=Inter:wght@400;500;600&display=swap">
<style>
:root{
  --lime:#cde000;
  --black:#000;
  --char:#1e1e1e;
  --card:#111;
  --line:#3a3a3a;
  --text:#fff;
  --muted:#b9b9b9;
  --head:"Orbitron",sans-serif;
  --body:"Inter",sans-serif;
}
*{box-sizing:border-box;margin:0;padding:0}
html,body{width:1200px;height:1200px;overflow:hidden;background:#fff}
.page{position:absolute;left:452px;top:0;width:476px;height:1932px;transform:scale(.62112);transform-origin:0 0;background:var(--black);color:var(--text);font-family:var(--body);overflow:hidden}
section,header,footer{position:absolute;left:0;width:476px}
.abs{position:absolute}
.photo{position:absolute}
.hl{color:var(--lime)}
.h2{font-family:var(--head);font-weight:500;font-size:11.5px;letter-spacing:.3px;text-transform:uppercase;line-height:16px;text-align:center}
.eyebrow{font-family:var(--head);font-size:3.6px;letter-spacing:.5px;color:var(--lime);text-transform:uppercase;display:flex;align-items:center;justify-content:center;gap:4px}
.eyebrow::before,.eyebrow::after{content:"";width:28px;height:1px;background:#fff}
.btn{position:absolute;height:14px;display:flex;align-items:center;gap:3px;padding:0 6px;font-size:3.8px;font-weight:600;text-transform:uppercase;letter-spacing:.2px;white-space:nowrap}
.btn-lime{background:var(--lime);color:#000}
.btn-ghost{border:1px solid #fff;color:#fff}
.btn-white{background:#fff;color:#000}
.p{font-size:4.2px;line-height:7px;color:#ddd}
.logo{display:flex;align-items:center;gap:3px;font-family:var(--head);font-weight:600;color:var(--lime);text-transform:uppercase}
.logo .mark{width:9px;height:9px;background:var(--lime)}

/* hero */
.hero{top:0;height:262px;background:linear-gradient(180deg,rgba(0,0,0,.15),rgba(0,0,0,.35) 60%,#000 100%),radial-gradient(ellipse at 70% 45%,#8a8a2a 0,#4d4f2c 30%,#3a4431 55%,#22281f 100%)}
.nav{top:6px;left:57px;width:364px;height:14px}
.nav .logo{position:absolute;left:0;top:2px;font-size:5px}
.nav ul{position:absolute;left:94px;top:4px;display:flex;gap:12px;list-style:none;font-size:3.6px;text-transform:uppercase;color:#ddd}
.nav ul li:first-child{color:var(--lime)}
.hero .tag{left:56px;top:85px;font-size:3.6px;font-weight:600;letter-spacing:.3px;text-transform:uppercase;display:flex;gap:3px;align-items:center}
.hero .tag i{width:4px;height:4px;border-radius:50%;background:var(--lime)}
.hero h1{left:56px;top:96px;font-family:var(--head);font-weight:500;font-size:17px;line-height:19px;text-transform:uppercase}
.hero .p{left:56px;top:143px;width:180px}

/* about */
.about{top:262px;height:229px;background:#000}
.badge{left:134px;top:97px;width:38px;height:38px;border-radius:50%;background:var(--lime);border:3px solid #1b1b1b;box-shadow:0 0 0 1px #444;display:flex;align-items:center;justify-content:center}
.about .eyebrow{left:268px;top:48px;justify-content:flex-start}
.about .eyebrow::before{display:none}
.about .eyebrow::after{width:100px}
.about .h2{left:268px;top:58px;text-align:left}
.about .p{left:268px;width:153px}

/* services */
.services{top:491px;height:315px;background:var(--char)}
.svc{top:85px;width:117px;height:141px;overflow:hidden;border:1px solid #2a2a2a}
.svc .shade{position:absolute;inset:0;background:linear-gradient(180deg,rgba(0,0,0,0) 40%,rgba(0,0,0,.85) 100%)}
.svc h3{position:absolute;left:6px;top:94px;font-family:var(--head);font-weight:500;font-size:6.5px;line-height:9px;text-transform:uppercase}
.svc p{position:absolute;left:6px;top:117px;width:92px;font-size:3.2px;line-height:5px;color:#ccc}
.pills{left:56px;top:240px;width:364px;display:grid;grid-template-columns:repeat(4,1fr);gap:4px 4px}
.pill{height:15px;border:1px solid #3c3c3c;background:#111;display:flex;align-items:center;justify-content:center;font-family:var(--head);font-size:3.6px;letter-spacing:.3px;text-transform:uppercase}

/* projects */
.projects{top:806px;height:360px;background:#000}

/* why */
.why{top:1166px;height:210px;background:var(--char)}
.why-card{top:86px;width:86px;height:82px;background:#0c0c0c;border:1px solid #333;text-align:center}
.why-card svg{margin-top:14px}
.why-card h4{font-family:var(--head);font-weight:500;font-size:5px;color:var(--lime);text-transform:uppercase;margin-top:2px;line-height:8px}
.why-card p{font-size:3.4px;line-height:5.5px;color:#ccc;padding:2px 6px 0}

/* testimonials */
.testi{top:1376px;height:224px;background:#000}
.t-card{top:92px;width:117px;height:89px;background:#1c1c1c;padding:8px 9px}
.stars{color:var(--lime);font-size:5px;letter-spacing:1.5px}
.t-card q{display:block;font-size:3.8px;line-height:6.3px;color:#ddd;margin-top:4px;height:40px;quotes:none}
.t-card hr{border:0;border-top:1px solid #333;margin:5px 0 4px}
.t-card b{display:block;font-size:3.4px;font-weight:600;text-transform:uppercase}
.t-card small{display:block;font-size:3px;color:#777}

/* cta */
.cta{top:1600px;height:140px;background:#000}
.cta .p{left:0;width:476px;text-align:center;top:69px}

/* footer */
.scape{top:1740px;height:80px;background:linear-gradient(180deg,#000 0,#141414 45%,#1c1c1c 100%)}
.footer{top:1810px;height:122px;background:linear-gradient(180deg,#1a1a1a,#202020)}
.footer h5{font-family:var(--head);font-weight:500;font-size:4.6px;color:var(--lime)}
.footer ul{list-style:none;font-size:3.3px;line-height:9px;color:#ccc;margin-top:4px}
.contact li{display:flex;align-items:center;gap:4px;line-height:12.5px}
.contact i{width:7px;height:7px;border:1px solid var(--lime);border-radius:50%}
.social{display:flex;gap:7px}
.social i{width:6px;height:6px;border-radius:50%;border:1px solid #ddd}
.copy{left:0;width:476px;top:110px;text-align:center;font-size:3px;color:#999}
</style>
</head>
<body>
<div class="page">

<header class="hero">
  <div class="photo" style="inset:0;background:radial-gradient(ellipse 35% 40% at 70% 40%,rgba(205,190,40,.35),transparent)" role="img" aria-label="Yellow mini excavator working on a residential block"></div>
  <nav class="nav abs">
    <div class="logo"><span class="mark"></span>Gullwind Stonecut</div>
    <ul><li>Home</li><li>About us</li><li>Services</li><li>Projects</li><li>Contact</li></ul>
    <span class="btn btn-lime" style="left:258px;top:0;height:13px">Get a quote</span>
    <span class="btn btn-white" style="left:305px;top:0;height:13px;width:59px">
      <svg width="6" height="6" viewBox="0 0 24 24"><circle cx="12" cy="12" r="11" fill="none" stroke="#000" stroke-width="2"/><path d="M8 7l2 0 1 3-1.5 1a8 8 0 0 0 4 4l1-1.5 3 1v2a2 2 0 0 1-2 1A10 10 0 0 1 7 9a2 2 0 0 1 1-2z" fill="#000"/></svg>+61 455 218 306</span>
  </nav>
  <div class="tag abs"><i></i>Perth, Western Australia</div>
  <h1 class="abs">Professional<br><span class="hl">Earthworks</span> &amp; Excavation</h1>
  <p class="p abs">From site preparation to trenching and demolition, Gullwind Stonecut Earthworks delivers reliable excavation services across the Perth metropolitan area. Built on precision, powered by experience.</p>
  <span class="btn btn-lime" style="left:56px;top:174px">Request a quote ↗</span>
  <span class="btn btn-ghost" style="left:125px;top:174px">View our works</span>
</header>

<section class="about">
  <div class="photo" style="left:56px;top:50px;width:96px;height:66px;background:linear-gradient(160deg,#6e8aa8,#6f8b3c 55%,#4d5a2a)" role="img" aria-label="Mini excavator on a grassy lot"></div>
  <div class="photo" style="left:154px;top:38px;width:96px;height:156px;background:linear-gradient(180deg,#7d97b2,#4f6b34 35%,#8a7c62 70%,#a6977c)" role="img" aria-label="Trench dug beside a fence line"></div>
  <div class="photo" style="left:74px;top:121px;width:78px;height:65px;background:linear-gradient(170deg,#7893ad,#5c6a3a 50%,#7a6a4c)" role="img" aria-label="Excavator clearing scrubland"></div>
  <div class="badge abs"><svg width="16" height="16" viewBox="0 0 24 24"><circle cx="12" cy="12" r="9" fill="none" stroke="#000" stroke-width="2"/><path d="M7.5 12l3 3 6-6" fill="none" stroke="#000" stroke-width="2.4"/></svg></div>
  <div class="eyebrow abs">About us</div>
  <h2 class="h2 abs">Building Perth's<br>Foundations</h2>
  <p class="p abs" style="top:98px">Gullwind Stonecut Earthworks is a Perth-based excavation company dedicated to delivering exceptional earthworks solutions. From residential projects to commercial developments, we bring the expertise and equipment needed to get the job done right.</p>
  <p class="p abs" style="top:133px">Our commitment to safety, quality, and customer satisfaction sets us apart. We work closely with builders, developers, and homeowners across the Perth metropolitan area to ensure every project meets the highest standards.</p>
  <span class="btn btn-lime" style="left:268px;top:171px">Learn more ↗</span>
</section>

<section class="services">
  <div class="eyebrow abs" style="left:0;width:476px;top:42px">What we do us</div>
  <h2 class="h2 abs" style="left:0;width:476px;top:53px">Our Services</h2>
  <div class="svc abs" style="left:56px">
    <div class="photo" style="inset:0;background:linear-gradient(160deg,#3a2a16,#7a4a1a 45%,#2a1a0c)" role="img" aria-label="Deep excavation pit with shoring"></div>
    <div class="shade"></div>
    <h3 class="hl">Site<br>Preparation</h3>
    <svg class="abs" style="left:97px;top:98px" width="12" height="12" viewBox="0 0 12 12"><circle cx="6" cy="6" r="6" fill="#cde000"/><path d="M4 8l4-4M5 4h3v3" stroke="#000" stroke-width=".9" fill="none"/></svg>
    <p>Complete site clearing, levelling, and preparation for residential and commercial construction projects.</p>
  </div>
  <div class="svc abs" style="left:180px">
    <div class="photo" style="inset:0;background:linear-gradient(170deg,#b85a34,#c9744a 40%,#8a3f22)" role="img" aria-label="Red soil trench with drainage pipe"></div>
    <div class="shade"></div>
    <h3>Trenching &amp;<br>Drainage</h3>
    <p>Precision trenching for utilities, stormwater drainage, and sewer systems with minimal disruption.</p>
  </div>
  <div class="svc abs" style="left:304px">
    <div class="photo" style="inset:0;background:linear-gradient(160deg,#aab3ba,#d4a21c 45%,#6b6a66)" role="img" aria-label="Yellow excavator bucket close-up"></div>
    <div class="shade"></div>
    <h3 style="top:94px">Demolition</h3>
    <p style="top:108px">Safe and efficient demolition of structures, concrete, and site obstacles.</p>
  </div>
  <div class="pills abs">
    <div class="pill">Rock Breaking</div><div class="pill">Pool Excavation</div><div class="pill">Land Clearing</div><div class="pill">Retaining Walls</div>
    <div class="pill">Driveway Preparation</div><div class="pill">Skid Steer Services</div><div class="pill">Soil Removal</div><div class="pill">Grading &amp; Leveling</div>
  </div>
</section>

<section class="projects">
  <div class="eyebrow abs" style="left:0;width:476px;top:42px">Portfolio</div>
  <h2 class="h2 abs" style="left:0;width:476px;top:53px">Some of our <span class="hl">Projects</span></h2>
  <div class="photo" style="left:92px;top:86px;width:110px;height:85px;background:linear-gradient(90deg,#8a5a36,#5a3a24 50%,#9a6a44)" role="img" aria-label="Narrow trench cut in clay"></div>
  <div class="photo" style="left:207px;top:86px;width:118px;height:85px;background:linear-gradient(180deg,#9ab0c4,#5d7a4e 45%,#a4553a 75%)" role="img" aria-label="Dozer on red earth below hills"></div>
  <div class="photo" style="left:331px;top:86px;width:72px;height:85px;background:linear-gradient(180deg,#c4d2de,#8a7a5a 60%,#a06a44)" role="img" aria-label="Excavator on a dirt mound"></div>
  <div class="photo" style="left:56px;top:176px;width:73px;height:84px;background:linear-gradient(180deg,#d8d4d0,#b49c8c 50%,#8a6a54)" role="img" aria-label="Flooded site with machinery"></div>
  <div class="photo" style="left:134px;top:176px;width:141px;height:111px;background:linear-gradient(180deg,#2e3a24,#4a4a2a 45%,#c28a24 65%,#8a5a34)" role="img" aria-label="Bulldozer clearing forest"></div>
  <div class="photo" style="left:280px;top:176px;width:108px;height:84px;background:linear-gradient(180deg,#b8c8d6,#a89a84 50%,#8a7058)" role="img" aria-label="Workers on a construction site"></div>
  <span class="btn btn-lime" style="left:204px;top:305px">View all projects ↗</span>
</section>

<section class="why">
  <div class="eyebrow abs" style="left:0;width:476px;top:43px">Why choose us</div>
  <h2 class="h2 abs" style="left:0;width:476px;top:54px">Building <span class="hl">Trust</span></h2>
  <div class="why-card abs" style="left:56px">
    <svg width="14" height="16" viewBox="0 0 14 16"><rect x="1" y="1" width="12" height="14" fill="none" stroke="#fff"/><path d="M4 9l2 2 4-4" stroke="#fff" fill="none"/></svg>
    <h4>Fully Insured</h4><p>Complete public liability and professional indemnity coverage for your peace of mind.</p>
  </div>
  <div class="why-card abs" style="left:149px">
    <svg width="16" height="16" viewBox="0 0 16 16"><circle cx="6" cy="5" r="3" fill="none" stroke="#fff"/><path d="M1 15c0-4 2-6 5-6s5 2 5 6" fill="none" stroke="#fff"/><circle cx="12" cy="11" r="3" fill="none" stroke="#fff"/></svg>
    <h4>On-Time Delivery</h4><p>We respect your timeline and deliver projects on schedule, every time.</p>
  </div>
  <div class="why-card abs" style="left:241px">
    <svg width="16" height="16" viewBox="0 0 16 16"><circle cx="8" cy="7" r="5" fill="none" stroke="#fff"/><path d="M5 12l-1 3 4-2 4 2-1-3" fill="none" stroke="#fff"/></svg>
    <h4>Quality First</h4><p>Precision workmanship and attention to detail on every job, big or small.</p>
  </div>
  <div class="why-card abs" style="left:334px">
    <svg width="16" height="14" viewBox="0 0 16 14" style="margin-top:10px"><rect x="1" y="1" width="14" height="10" fill="none" stroke="#fff"/><path d="M3 4h6M3 7h4" stroke="#fff"/><circle cx="12" cy="8" r="2" fill="none" stroke="#fff"/></svg>
    <h4>Licensed<br>Operators</h4><p>Experienced and certified operators with extensive industry knowledge.</p>
  </div>
</section>

<section class="testi">
  <div class="eyebrow abs" style="left:0;width:476px;top:33px">Testimonials</div>
  <h2 class="h2 abs" style="left:0;width:476px;top:44px">What our clients<br><span class="hl">say about us</span></h2>
  <div class="t-card abs" style="left:56px"><div class="stars">★★★★★</div><q>"Gullwind Stonecut delivered exceptional site prep for our housing development. Professional, on time, and the quality of work was outstanding. Highly recommend for any earthworks project."</q><hr><b>Owen Harlow</b><small>Builder, Harlow Constructions</small></div>
  <div class="t-card abs" style="left:180px"><div class="stars">★★★★★</div><q>"We've used Gullwind Stonecut on multiple projects across Perth. Their attention to detail and reliability is unmatched. The team goes above and beyond every time."</q><hr><b>Priya Delacourt</b><small>Property Developer</small></div>
  <div class="t-card abs" style="left:304px"><div class="stars">★★★★★</div><q>"Needed trenching work for my new pool installation. The crew was friendly, efficient, and left the site spotless. Fair pricing and great communication throughout."</q><hr><b>Tomas Brandt</b><small>Homeowner, Ridgefall</small></div>
  <svg class="abs" style="left:224px;top:196px" width="30" height="2"><rect width="12" height="1.5" fill="#cde000"/><circle cx="17" cy=".8" r=".8" fill="#777"/><circle cx="21" cy=".8" r=".8" fill="#777"/><circle cx="25" cy=".8" r=".8" fill="#777"/></svg>
</section>

<section class="cta">
  <h2 class="h2 abs" style="left:0;width:476px;top:26px">Ready to<br><span class="hl">Get Started ?</span></h2>
  <p class="p abs">Whether you need site preparation, trenching, or demolition services, we're here to help.<br>Get in touch for a free, no-obligation quote on your next earthworks project.</p>
  <span class="btn btn-lime" style="left:192px;top:91px">Get a quote</span>
  <span class="btn btn-white" style="left:240px;top:91px"><svg width="6" height="6" viewBox="0 0 24 24"><circle cx="12" cy="12" r="11" fill="none" stroke="#000" stroke-width="2"/></svg>Call now</span>
</section>

<div class="scape abs" role="img" aria-label="Silhouettes of excavators and loaders on a ridge"></div>

<footer class="footer">
  <div class="logo abs" style="left:70px;top:40px;font-size:5px">Gullwind<br>Stonecut</div>
  <div class="social abs" style="left:74px;top:73px"><i></i><i></i><i></i><i></i></div>
  <div class="abs" style="left:146px;top:24px"><h5>Quick Links</h5><ul><li>Home</li><li>About Us</li><li>Services</li><li>Projects</li><li>Testimonials</li><li>Contact</li></ul></div>
  <div class="abs" style="left:212px;top:24px"><h5>Services</h5><ul><li>Site Preparation</li><li>Trenching and Drainage</li><li>Demolition</li><li>Land Clearing</li><li>Skid Steer Services</li><li>Grading and Leveling</li></ul></div>
  <div class="abs" style="left:279px;top:24px"><h5>&nbsp;</h5><ul><li>Pool Excavation</li><li>Rock Breaking</li><li>Driveway Preparation</li><li>Soil Removal</li><li>Retaining Walls</li></ul></div>
  <div class="abs contact" style="left:346px;top:24px"><h5>Contact Us</h5><ul><li><i></i>+61 455 218 306</li><li><i></i>admin@gullwindstonecut.com.au</li><li><i></i>Ridgefall, WA, Australia</li></ul></div>
  <div class="copy abs">© 2025 Gullwind Stonecut Earthworks. All rights reserved.</div>
</footer>

</div>
</body>
</html>
```